Spannish marketing agency needs redesign of powerpoint presentation for client acquisition

We want to redesign our powerpoint presentation. We use this presentation to show our clients how we work. WE NEED IT TO BE IN POWERPOINT FORMAT
The style should match the style of our logo and story brand, but apart from that we want designers to get creative.
The project must be in powerpoint format. The project must be in powerpoint format
Baja calidad de diseño
Small and medium size business owners
Digital marketing

```html
<!DOCTYPE html>
<html lang="es">
<head>
<meta charset="UTF-8">
<title>Plan estratégico de marketing</title>
<link href="https://fonts.googleapis.com/css2?family=Montserrat:wght@400;700&display=swap" rel="stylesheet">
<style>
  :root {
    --brand-blue: #0b63d1;
    --text-dark: #1f2328;
    --navy: #15233a;
    --panel-grey: #dfe1e5;
    --white: #ffffff;
  }
  * { margin: 0; padding: 0; box-sizing: border-box; }
  html, body {
    width: 1200px;
    height: 675px;
    overflow: hidden;
    background: var(--white);
  }
  .slide {
    position: relative;
    width: 1200px;
    height: 675px;
    background: var(--white);
    font-family: "Montserrat", sans-serif;
  }
  .content {
    position: absolute;
    left: 57px;
    top: 103px;
    width: 491px;
  }
  .title {
    color: var(--brand-blue);
    font-weight: 700;
    font-size: 31px;
    line-height: 37.5px;
    letter-spacing: 0.12em;
    text-transform: uppercase;
  }
  .benefits {
    list-style: none;
    margin-top: 47px;
    color: var(--text-dark);
    font-weight: 400;
    font-size: 18.2px;
    line-height: 24px;
  }
  .benefits li {
    text-align: justify;
    text-align-last: left;
  }
  .benefits li::before {
    content: "• ";
  }
  .visual {
    position: absolute;
    left: 600px;
    top: 0;
    width: 600px;
    height: 675px;
    background:
      radial-gradient(ellipse 190px 120px at 300px 60px, rgba(30,120,230,0.55), rgba(30,120,230,0) 100%),
      radial-gradient(ellipse 210px 230px at 300px 400px, rgba(255,255,255,0.9), rgba(255,255,255,0) 100%),
      radial-gradient(ellipse 200px 140px at 310px 600px, rgba(20,115,230,0.6), rgba(20,115,230,0) 100%),
      var(--panel-grey);
  }
  .brand-name {
    position: absolute;
    left: 1034px;
    top: 54px;
    color: var(--navy);
    font-family: "Montserrat", sans-serif;
    font-weight: 400;
    font-size: 21px;
    letter-spacing: 0.12em;
  }
</style>
</head>
<body>
<main class="slide">
  <section class="content">
    <h1 class="title">¿En qué puede ayudar a tu empresa un plan estratégico de marketing?</h1>
    <ul class="benefits">
      <li>Definir la identidad visual y comunicativa de la empresa.</li>
      <li>Definir los objetivos que se quieren conseguir.</li>
      <li>Diseñar estrategias de captación, conversión y fidelización de los clientes.</li>
      <li>Designar las plataformas que se van a utilizar para atraer y gestionar a los clientes.</li>
      <li>Estrategia de producción de contenidos en redes sociales.</li>
      <li>Designar las métricas más importantes en cada uno de los procesos y cómo medirlas.</li>
      <li>Formas de automatizar procesos en la empresa.</li>
    </ul>
  </section>
  <div class="visual" role="img" aria-label="Ilustración 3D de cubos azules y blancos que se ensamblan formando un bloque"></div>
  <div class="brand-name">VELARIS</div>
</main>
</body>
</html>
```